Business card

Looking for modern clean business card off logo below. Very important to be clean and professional but want fun as well

Industry/Entity Type

Business

```html
<!DOCTYPE html>
<html lang="en">
<head>
<meta charset="utf-8">
<title>Crest Homes – Business Card</title>
<link rel="stylesheet" href="https://fonts.googleapis.com/css2?family=Oswald:wght@600&family=Open+Sans:wght@400;600&display=swap">
<style>
  :root {
    --brand-blue: #4fb0d0;
    --ink-dark: #4a4a4c;
    --ink-mid: #555558;
    --card-white: #ffffff;
    --backdrop: #e6e7e9;
  }
  * { margin: 0; padding: 0; box-sizing: border-box; }
  html, body { width: 1200px; height: 900px; overflow: hidden; }
  body {
    background: var(--backdrop);
    font-family: "Open Sans", sans-serif;
    position: relative;
  }
  .card {
    position: absolute;
    left: 250px;
    width: 700px;
    height: 400px;
    background: var(--card-white);
    border-radius: 28px;
    overflow: hidden;
    box-shadow: 0 6px 18px rgba(0,0,0,0.12);
  }
  .card-back { top: 40px; }
  .card-front { top: 470px; }

  .brand { display: flex; align-items: center; gap: 18px; }
  .brand-dot {
    width: 58px; height: 58px; border-radius: 50%;
    background: var(--brand-blue);
    flex: none;
  }
  .brand-name {
    font-family: "Oswald", sans-serif;
    font-weight: 600;
    font-size: 44px;
    line-height: 1;
    letter-spacing: 0.5px;
    color: var(--ink-dark);
    text-transform: uppercase;
  }
  .brand-tagline {
    font-size: 14px;
    color: var(--ink-mid);
    margin-top: 4px;
    letter-spacing: 0.2px;
  }

  .card-back .brand {
    position: absolute;
    left: 60px; top: 160px;
  }

  .card-front .brand {
    position: absolute;
    left: 40px; top: 40px;
  }

  .person {
    position: absolute;
    left: 140px; top: 150px;
  }
  .person-name {
    font-size: 22px;
    font-weight: 600;
    color: var(--brand-blue);
    letter-spacing: 0.3px;
  }
  .person-title {
    font-size: 20px;
    color: var(--ink-mid);
    margin-top: -2px;
  }
  .contact-list {
    list-style: none;
    margin-top: 12px;
  }
  .contact-list li {
    display: flex;
    align-items: center;
    gap: 12px;
    font-size: 19px;
    color: var(--ink-mid);
    line-height: 28px;
  }
  .contact-icon { width: 16px; height: 16px; flex: none; fill: var(--brand-blue); }

  .address-band {
    position: absolute;
    left: 0; right: 0; bottom: 0;
    height: 58px;
    background: var(--brand-blue);
    color: var(--card-white);
    font-size: 19px;
    letter-spacing: 0.4px;
    display: flex;
    align-items: center;
    justify-content: center;
  }
</style>
</head>
<body>

  <section class="card card-back" aria-label="Card back">
    <div class="brand">
      <span class="brand-dot"></span>
      <div>
        <div class="brand-name">Crest Homes</div>
        <div class="brand-tagline">Property Management and Real Estate</div>
      </div>
    </div>
  </section>

  <section class="card card-front" aria-label="Card front">
    <div class="brand">
      <span class="brand-dot"></span>
      <div>
        <div class="brand-name">Crest Homes</div>
        <div class="brand-tagline">Property Management and Real Estate</div>
      </div>
    </div>

    <div class="person">
      <div class="person-name">Daniel Marlow</div>
      <div class="person-title">managing director</div>
      <ul class="contact-list">
        <li>
          <svg class="contact-icon" viewBox="0 0 16 16" aria-hidden="true"><path d="M4 0h8a1.5 1.5 0 0 1 1.5 1.5v13A1.5 1.5 0 0 1 12 16H4a1.5 1.5 0 0 1-1.5-1.5v-13A1.5 1.5 0 0 1 4 0zm0.5 2v10h7V2zm3.5 11a1 1 0 1 0 0 2 1 1 0 0 0 0-2z"/></svg>
          777 214 36 90
        </li>
        <li>
          <svg class="contact-icon" viewBox="0 0 16 16" aria-hidden="true"><path d="M4 0h8v4H4zM1 5h14a1 1 0 0 1 1 1v6h-3v4H3v-4H0V6a1 1 0 0 1 1-1zm3.5 6v3.5h7V11z"/></svg>
          777 214 36 91
        </li>
        <li>
          <svg class="contact-icon" viewBox="0 0 16 16" aria-hidden="true"><path d="M0 3h16v1.2L8 9 0 4.2zM0 5.8l8 4.8 8-4.8V13H0z"/></svg>
          dmarlow@cresthomes.com
        </li>
        <li>
          <svg class="contact-icon" viewBox="0 0 16 16" aria-hidden="true"><path d="M8 0a8 8 0 1 0 0 16A8 8 0 0 0 8 0zm-1 1.6V5H4.2A6.5 6.5 0 0 1 7 1.6zm2 0A6.5 6.5 0 0 1 11.8 5H9zM3.6 6.5H7v3H3.6a6.5 6.5 0 0 1 0-3zm5.4 0h3.4a6.5 6.5 0 0 1 0 3H9zM4.2 11H7v3.4A6.5 6.5 0 0 1 4.2 11zM9 11h2.8A6.5 6.5 0 0 1 9 14.4z"/></svg>
          www.cresthomes.com
        </li>
      </ul>
    </div>

    <div class="address-band">48 Maple Lane, Riverton, Ohio 45102</div>
  </section>

</body>
</html>
```